Luxury Lifestyle service requires name card

Logo of my company has to be on the left side of the card. (Blue logo)Name and information preferably on the right side.QR code inclusion would be great , Gold logo if it can be included at the back of the card would be great too- we are a luxury lifestyle concierge company catering to the high net worth clients.

Target Market(s)

high net worth customers / luxury

Industry/Entity Type

Business Service

Contact Information for Business Card

name
contact
email
website

Font styles to use
Serif

Colors
0255a3
3176b5
85abd2
0492cd
33a6d7
85cae6
cee9f5

Requirements
Must have
• Logo of my company has to be on the left side of the card. (Blue logo)
• Name and information on the right side.
Nice to have
• QR code inclusion would be great
Should not have
• Do not use colours :- red , purple , orange , yellow
• background card colour : do not use black

```html
<!DOCTYPE html>
<html lang="en">
<head>
<meta charset="utf-8">
<title>Vellaro Daily – Business Card</title>
<link rel="stylesheet" href="https://fonts.googleapis.com/css2?family=Cinzel:wght@400&family=Lora:wght@400;500&display=swap">
<style>
  :root {
    --canvas-bg: #bfbfbf;
    --card-navy: #0b3a6e;
    --gold: #c9a227;
    --wordmark-light: #e4e9f0;
    --card-light: #f2f2f1;
    --wordmark-dark: #34383c;
    --brand-blue: #0492cd;
    --blue-start: #0aaedc;
    --blue-end: #0270bf;
    --accent-cyan: #16d2e2;
    --ink: #14202c;
    --qr-panel: #ffffff;
  }
  * { box-sizing: border-box; margin: 0; padding: 0; }
  html, body { width: 1200px; height: 576px; overflow: hidden; }
  body { background: var(--canvas-bg); position: relative; }

  .card {
    position: absolute;
    top: 139px;
    width: 484px;
    height: 291px;
    border-radius: 13px;
    overflow: hidden;
  }
  .card--back { left: 82px; background: var(--card-navy); }
  .card--front { left: 602px; background: var(--card-light); }

  .brand__dot { position: absolute; border-radius: 50%; transform: translateX(-50%); }
  .card--back .brand__dot { left: 242px; top: 84px; width: 74px; height: 74px; background: var(--gold); }
  .card--front .brand__dot { left: 111px; top: 90px; width: 70px; height: 70px; background: var(--brand-blue); }

  .brand__name {
    position: absolute;
    transform: translateX(-50%);
    font-family: "Cinzel", serif;
    font-weight: 400;
    white-space: nowrap;
    letter-spacing: 0.5px;
    line-height: 1;
  }
  .card--back .brand__name { left: 242px; top: 197px; font-size: 22px; color: var(--wordmark-light); }
  .card--front .brand__name { left: 111px; top: 188px; font-size: 19px; color: var(--wordmark-dark); }

  .front-bg { position: absolute; inset: 0; width: 100%; height: 100%; }

  .details {
    position: absolute;
    left: 269px;
    top: 83px;
    font-family: "Lora", serif;
    color: var(--ink);
  }
  .details__name { font-size: 20px; font-weight: 400; line-height: 1.2; }
  .details__title { font-size: 12px; font-weight: 400; margin-top: 4px; }
  .contact-list { list-style: none; margin-top: 26px; }
  .contact-list li {
    display: flex;
    align-items: center;
    font-size: 12px;
    font-weight: 400;
    height: 18.5px;
    white-space: nowrap;
  }
  .contact-list svg { width: 10px; height: 10px; margin-right: 13px; fill: var(--ink); flex: none; }

  .qr-area {
    position: absolute;
    left: 412px;
    top: 222px;
    width: 52px;
    height: 52px;
    border-radius: 4px;
    background: var(--qr-panel);
  }
</style>
</head>
<body>

  <section class="card card--back">
    <span class="brand__dot"></span>
    <span class="brand__name">VELLARO DAILY</span>
  </section>

  <section class="card card--front">
    <svg class="front-bg" viewBox="0 0 484 291" preserveAspectRatio="none" aria-hidden="true">
      <defs>
        <linearGradient id="panel-blue" x1="0" y1="0" x2="1" y2="0.3">
          <stop offset="0" stop-color="#0aaedc"/>
          <stop offset="1" stop-color="#0270bf"/>
        </linearGradient>
      </defs>
      <path d="M190 0 Q272 146 190 291 L484 291 L484 0 Z" fill="url(#panel-blue)"/>
      <path d="M190 0 Q272 146 190 291 L206 291 Q280 146 198 0 Z" fill="#16d2e2"/>
    </svg>

    <span class="brand__dot"></span>
    <span class="brand__name">VELLARO DAILY</span>

    <div class="details">
      <h1 class="details__name">Adrian Vell</h1>
      <p class="details__title">Managing Director</p>
      <ul class="contact-list">
        <li>
          <svg viewBox="0 0 10 10"><path d="M0 3 Q5 0 10 3 L9 4.5 L7 4 L7 3 Q5 2.3 3 3 L3 4 L1 4.5 Z M2 5 L8 5 L9 9 L1 9 Z"/></svg>
          +100 5550 2417
        </li>
        <li>
          <svg viewBox="0 0 10 10"><path d="M0 2 L10 2 L5 6 Z M0 3 L5 7 L10 3 L10 8.5 L0 8.5 Z"/></svg>
          adrian@vellarodaily.com
        </li>
        <li>
          <svg viewBox="0 0 10 10"><path d="M5 0.5 A4.5 4.5 0 1 0 5 9.5 A4.5 4.5 0 1 0 5 0.5 Z M5 1.5 Q3.3 5 5 8.5 Q6.7 5 5 1.5 Z M1.5 4.4 L8.5 4.4 L8.5 5.6 L1.5 5.6 Z" fill-rule="evenodd"/></svg>
          www.vellarodaily.com
        </li>
      </ul>
    </div>

    <div class="qr-area" role="img" aria-label="QR code area"></div>
  </section>

</body>
</html>
```